Website for a financial survey consultancy

WHO WE ARE
We're a niche HR consultancy specialising in salary comparison surveys for the financial asset management industry. We position ourselves as a small, highly responsive organisation with a strong personal relationship with each of our 50+ blue-chip clients.

WHAT WE DO
Our business is 80% surveys (= products), 20% consultancy (= services). The surveys are a set of online products which clients interact with to find the information they are interested in.

WHAT WE WANT
We are completely revising our existing marketing website and need a new up-to-date look and feel for the site. We want you to design 2 web pages
- Home page
- Internal content page

More details below in Must Have Priorities.

REFERENCE SITES
- www.tallowmere.com - nice background image
- www.quimbelt.com - ignoring the animations
- www.palvastro.com
- www.dulmiko.com - clean, fresh, styly but prob not corporate enough
- www.orvettagrove.com - spacious, beautiful, slightly dated tho
- www.plinzer.co.uk - ignore the colours. Like the simplicity, larger font size (although want to stick with sans-serif fonts for main content)

DELIVERABLES
The final designs should be delivered as one or more PSD files with clearly named layers. All design elements and treatments should be separated out, for example use adjustment layers rather than applied (and subsequently irreversible) adjustments, strokes, shading, etc.

WHAT NEXT
I'll be monitoring the contest every day and can respond to questions fast. You can IM me on Skype or MSN.

Reason: Hi folks,

I am extending the deadline to this project as I am travelling this week and therefore will not be able to make a final decision until next Monday. I will try and provide further feedback over the course of this week but I am only going to be online occasionally so be prepared to wait a few days for a reply from me.

Thanks for all the designs so far.

Owen

Target Market(s)

In order of importance, most important first

1. Potential customers - UK & US financial industry HR professionals, short on time. Heard about us already, want to find out more about what we do, confirm relevance for their needs. Core goal - establish credibility: are we properly resourced, will we be around for years to come, are we *real*.

2. Existing customers - UK & US financial industry professionals, short on time, under pressure, want results quickly, minimum faff, expect high quality, slickly presented information. Primary action: login and use surveys.

3. Industry professionals/researchers - probably arriving through blog content, looking to browse and hoover information. Valuable for their ability to spread awareness of who we are amongst their peers.

Industry/Entity Type

Financial

Requirements
Must have
• GENERAL
Style cues - Corporate, professional, financial, stylish, slick, clean, spacious, light
Size - standard 960px grid

NAVIGATION
- [ Home | About us | Surveys | Consulting | Blog ]
- Sub-nav (roll-over dropdown) on About Us, Surveys & Consulting

ALL PAGES
- Site navigation
- Client login (on screen permanently or link to ajaxy in-page pop-up)
- Footer section
- Existing logo (attached)* - this is obviously an important reference point in the design, esp colour

HOME PAGE
- Communicate (link thru to?) survey/consulting split
- Large photo(s)/backdrop (2-3 interchangeable options ideally). Please consider what rights agreement will be necessary for any photos you include in your design.
- Possibly bigger more prominent version of logo
- Strap line/sentence - "Focussed data is the key to success"
- 3 recent blog posts (should look good with and without blog post images)
- Free downloadable PDF research report + supporting blurb

INTERNAL PAGE
- Page title
- Content - typical page will be less than one screenfull
- Level 1 sub-heading
- Level 2 sub-heading
- Bulleted list
- Content supporting image (any image will do - interested in placement, borders (if any), spacing, caption, etc)
- 'Do something' button

* Note: there is some internal debate about this logo at the moment. Some (me) are keen for it to change, some (not me!) are not. If you have an web page design idea/concept that requires an evolution of the logo, go ahead and evolve it. We can explore this further in the design process as necessary, but don't sweat it.
Nice to have
• Values to communicate
- Knowledgeable
- Professional
- Secure
- Personal
- Experienced
- Financial industry specific
- Accurate
- Reliable
Should not have
• - Search box
- Social media links, other than RSS feed button (discrete)

```html
<!DOCTYPE html>
<html lang="en">
<head>
<meta charset="utf-8">
<title>Norvane – About Us</title>
<link href="https://fonts.googleapis.com/css2?family=Arimo:wght@400;700&display=swap" rel="stylesheet">
<style>
:root{
  --brand:#680a0a;
  --brand-text:#5c0c0c;
  --body-blue:#2b6a9c;
  --ink:#3a3a3a;
  --panel:#f7f7f7;
  --nav-bg:#dcdcdc;
  --rule:#b9b9b9;
  --footer-bg:#ffffff;
  --base-bar:#262626;
}
*{box-sizing:border-box;margin:0;padding:0}
html,body{width:1200px;height:892px;overflow:hidden}
body{position:relative;font-family:"Arimo",Arial,sans-serif;background:var(--footer-bg);color:var(--ink)}
.backdrop{position:absolute;left:0;top:0;width:1200px;height:697px;
  background:linear-gradient(180deg,#7fb4da 0%,#9cc7e3 40%,#b9d3e3 70%,#8aa7b8 100%)}
.client-login{position:absolute;left:968px;top:8px;width:84px;height:30px;
  background:linear-gradient(#8fbfdc,#6fa4c8);color:#fff;font-size:13px;
  display:flex;align-items:center;justify-content:center;text-decoration:none}
.brand{position:absolute;left:167px;top:41px;width:120px}
.brand-square{display:block;width:120px;height:117px;background:var(--brand)}
.brand-name{display:block;margin-top:14px;text-align:center;font-size:30px;color:var(--brand);font-weight:400;letter-spacing:1px}
.main-nav{position:absolute;left:168px;top:321px;width:119px;list-style:none}
.main-nav li{height:36px;margin-bottom:1.6px;background:var(--nav-bg)}
.main-nav a{display:block;height:100%;padding-left:19px;line-height:36px;font-size:13px;color:var(--brand-text);text-decoration:none}
.main-nav .is-active{background:var(--brand)}
.main-nav .is-active a{color:#fff}
.page-title{position:absolute;left:305px;top:123px;font-size:21px;font-weight:400;color:#fff}
.title-rule{position:absolute;left:303px;top:154px;width:749px;height:4px;background:var(--brand)}
.banner{position:absolute;left:304px;top:158px;width:748px;height:163px;
  background:linear-gradient(90deg,#c9ddef 0%,#a9c8e6 45%,#9fc2e8 100%)}
.content{position:absolute;left:304px;top:321px;width:748px;height:362px;background:var(--panel);padding:18px 10px 0 10px}
.content h2{font-size:13.5px;font-weight:400;color:var(--brand-text);margin-left:2px;margin-bottom:4px}
.content p{font-size:11.5px;line-height:17px;color:var(--body-blue)}
.content .lead{margin-bottom:21px}
.bullets{list-style:none;margin:2px 0 9px 0}
.bullets li{position:relative;padding-left:21px;font-size:11.5px;line-height:18.8px;color:var(--ink)}
.bullets li::before{content:"";position:absolute;left:4px;top:6px;border-left:4px solid var(--brand);border-top:3px solid transparent;border-bottom:3px solid transparent}
.footer{position:absolute;left:0;top:697px;width:1200px;height:186px;background:var(--footer-bg)}
.footer h3{font-size:16px;font-weight:400;color:var(--brand-text);margin-bottom:6px}
.footer-col{position:absolute;top:17px;font-size:11.5px;line-height:15px;color:var(--ink)}
.blog-col{left:168px;width:253px}
.blog-item{position:relative;padding:0 0 9px 11px;margin-bottom:9px;border-bottom:1px solid var(--rule)}
.blog-item:last-child{border-bottom:none}
.blog-item::before{content:"";position:absolute;left:2px;top:3px;border-left:4px solid var(--brand);border-top:4px solid transparent;border-bottom:4px solid transparent}
.learn-more{color:var(--brand);font-size:10px;text-decoration:underline}
.download-col{left:459px;width:250px}
.download-col p{padding-left:2px}
.download-btn{position:absolute;left:0;top:102px;width:246px;height:47px;border-radius:3px;
  background:linear-gradient(#9cc7e6,#6fa6cf);display:flex;align-items:center;text-decoration:none}
.download-icon{width:38px;height:41px;margin-left:4px;background:#f2f2f2;border-radius:2px;display:flex;align-items:center;justify-content:center}
.download-icon span{display:block;width:26px;height:26px;background:#c0201a}
.download-label{margin-left:19px;color:#fff;font-size:15.5px;font-weight:700;line-height:14px}
.contact-col{left:732px;width:200px}
.contact-col address{font-style:normal;padding-left:2px}
.contact-col .email{margin-top:15px;padding-left:2px}
.copyright{margin-top:18px;font-size:9.5px;color:var(--brand);padding-left:2px}
.footer-brand{position:absolute;left:980px;top:17px;width:73px}
.footer-brand .brand-square{width:73px;height:73px}
.footer-brand .brand-name{font-size:17px;margin-top:10px}
.base-bar{position:absolute;left:0;top:883px;width:1200px;height:9px;background:var(--base-bar)}
</style>
</head>
<body>
<div class="backdrop" role="img" aria-label="Photo of a red suspension bridge over a bay beneath a light blue sky"></div>

<a class="client-login" href="#">Client Login</a>

<div class="brand">
  <span class="brand-square"></span>
  <span class="brand-name">Norvane</span>
</div>

<ul class="main-nav">
  <li><a href="#">HOME</a></li>
  <li class="is-active"><a href="#">ABOUT US</a></li>
  <li><a href="#">SURVEYS</a></li>
  <li><a href="#">CONSULTING</a></li>
  <li><a href="#">BLOG</a></li>
</ul>

<h1 class="page-title">ABOUT US</h1>
<div class="title-rule"></div>
<div class="banner" role="img" aria-label="Business people silhouettes shaking hands in front of a pale blue world map"></div>

<main class="content">
  <h2>VESTIBULUM ALIQUET VOLUTPAT</h2>
  <p class="lead">Lorem ipsum dolor sit amet, consectetur adipiscing elit. Nunc sed lorem dui. Sed quis nulla ac mauris lobortis imperdiet. Mauris quis augue in arcu pulvinar sollicitudin id non tellus. Sed sit amet orci sed arcu viverra vehicula. Phasellus in nibh nisl. Aenean non nisl quam. Phasellus id purus non eros pretium sagittis. Aenean in aliquam lectus. Duis blandit est rutrum libero pulvinar non elementum dui tristique. Morbi sit amet nibh mauris, in mattis ipsum. Ut placerat molestie ipsum lobortis tincidunt. Mauris non nulla massa.</p>
  <h2>CONSECTETUR ARDIPISCING</h2>
  <ul class="bullets">
    <li>Lorem ipsum dolor sit amet, consectetur adipiscing elit.</li>
    <li>Vestibulum aliquet volutpat velit, id fringilla arcu dignissim nec.</li>
    <li>Donec pulvinar mi fringilla tellus semper ac varius nisl posuere.</li>
    <li>Cras aliquam semper diam, ut lacinia ipsum semper ut.</li>
    <li>Sed porta blandit enim, id suscipit purus aliquet ac.</li>
    <li>Nunc congue felis mollis augue convallis accumsan.</li>
    <li>Proin eu nisi nulla, sit amet tincidunt sapien.</li>
  </ul>
  <p>Duis blandit est rutrum libero pulvinar non elementum dui tristique. Morbi sit amet nibh mauris, in mattis ipsum. Ut placerat molestie ipsum lobortis tincidunt. Mauris non nulla massa. Lorem ipsum dolor sit amet, consectetur adipiscing elit. Nunc sed lorem dui. Sed quis nulla ac mauris lobortis imperdiet. Mauris quis augue in arcu pulvinar sollicitudin id non tellus.</p>
</main>

<footer class="footer">
  <section class="footer-col blog-col">
    <h3>BLOG</h3>
    <div class="blog-item">Lorem ipsum dolor sit amet, consectetur adipiscing elit. <a class="learn-more" href="#">LEARN MORE</a></div>
    <div class="blog-item">Morbi a purus vel sem accumsan varius eget ut erat. <a class="learn-more" href="#">LEARN MORE</a></div>
    <div class="blog-item">Class aptent taciti sociosqu ad litora torquent per conubia nostra. <a class="learn-more" href="#">LEARN MORE</a></div>
  </section>

  <section class="footer-col download-col">
    <h3>FREE Download</h3>
    <p>er inceptos himenaeos. Pellentesque habitant morbi tristique senectus et netus et malesuada fames ac turpis egestas. Aliquam erat volutpat. Maecenas dapibus</p>
    <a class="download-btn" href="#">
      <span class="download-icon"><span></span></span>
      <span class="download-label">RESEARCH REPORT +<br>SUPPORTING BLURB</span>
    </a>
  </section>

  <section class="footer-col contact-col">
    <h3>Contact Us</h3>
    <address>Norvane<br>Suite 210 - 845 Larch Ave. N.W.<br>Cityname, State Name<br>USA</address>
    <p class="email">E-mail: contact@norvane.com</p>
    <p class="copyright">© 2011 Norvane.com. All rights reserved</p>
  </section>

  <div class="footer-brand">
    <span class="brand-square"></span>
    <span class="brand-name">Norvane</span>
  </div>
</footer>
<div class="base-bar"></div>
</body>
</html>
```